Business Card design for law firm = Juriskite Australia

We are seeking a new design for our business cards.
We are keeping our logo, which is attached.
We need space for
Name
Title
Address is , which is
Level 14
82 Penhallow Street
Sydney NSW 2000
Phone :
Mobile :
Fax :
Email :
DX :
website www.juriskite.com.au

Industry/Entity Type

Law Firm / Banking and Finance

Contact Information for Business Card

We are seeking a new design for our business cards. We are keeping our logo. We need space for Name Title Address is Level 14 82 Penhallow Street Sydney NSW 2000 Phone Mobile Fax Email DX website www.juriskite.com.au

Colors
0054AA
0677BA
7BADD7
CADEEF
E8F1F8

Requirements
Must have
• see our website for general feel www.juriskite.com.au

```html
<!DOCTYPE html>
<html lang="en">
<head>
<meta charset="utf-8">
<title>Juriskite Australia – Business Card</title>
<link rel="stylesheet" href="https://fonts.googleapis.com/css2?family=EB+Garamond:wght@500;600&family=Montserrat:wght@400;500&display=swap">
<style>
  :root {
    --navy: #0b4bb3;
    --sky: #0a88cc;
    --ink: #4a4a4a;
    --paper: #ffffff;
    --backdrop: #adadad;
    --serif: "EB Garamond", "Times New Roman", serif;
    --sans: "Montserrat", Arial, sans-serif;
  }
  * { box-sizing: border-box; margin: 0; padding: 0; }
  html, body { width: 1200px; height: 1056px; overflow: hidden; }
  body { background: var(--backdrop); position: relative; font-family: var(--sans); }

  .card {
    position: absolute;
    left: 220px;
    width: 760px;
    height: 434px;
    background: var(--paper);
    box-shadow: 0 18px 40px rgba(0,0,0,0.22);
    overflow: hidden;
  }
  .card--front { top: 50px; }
  .card--back { top: 562px; }

  /* name lockup: plain square beside the name */
  .brand { position: absolute; display: flex; align-items: center; }
  .brand__square { background: var(--sky); flex: none; }
  .brand__name {
    font-family: var(--serif);
    font-weight: 500;
    color: var(--navy);
    line-height: 1;
    white-space: nowrap;
  }
  .tagline {
    position: absolute;
    font-family: var(--sans);
    font-weight: 400;
    color: var(--sky);
    letter-spacing: 2px;
    white-space: nowrap;
  }

  .card--front .brand { left: 60px; top: 176px; gap: 16px; }
  .card--front .brand__square { width: 30px; height: 30px; }
  .card--front .brand__name { font-size: 62px; }
  .card--front .tagline { left: 62px; top: 262px; font-size: 18px; }

  .address-band {
    position: absolute;
    left: 0; right: 0;
    top: 354px;
    height: 40px;
    background: var(--sky);
    color: var(--paper);
    font-size: 15px;
    font-weight: 500;
    letter-spacing: 4px;
    line-height: 40px;
    padding-left: 62px;
    white-space: nowrap;
  }

  .contact { position: absolute; left: 450px; top: 78px; }
  .contact__name {
    font-family: var(--serif);
    font-weight: 600;
    font-size: 40px;
    color: var(--navy);
    line-height: 1.05;
  }
  .contact__title {
    font-size: 17px;
    color: var(--ink);
    letter-spacing: 1px;
    margin: 4px 0 18px;
  }
  .contact__list { list-style: none; }
  .contact__item {
    display: flex;
    align-items: center;
    gap: 10px;
    font-size: 14.5px;
    color: var(--ink);
    height: 30px;
  }
  .contact__icon { width: 20px; height: 20px; flex: none; }

  .card--back .brand { left: 200px; top: 160px; gap: 18px; }
  .card--back .brand__square { width: 36px; height: 36px; }
  .card--back .brand__name { font-size: 76px; }
  .card--back .tagline { left: 256px; top: 260px; font-size: 20px; }
</style>
</head>
<body>

<section class="card card--front" aria-label="Business card front">
  <div class="brand">
    <span class="brand__square"></span>
    <span class="brand__name">Juriskite</span>
  </div>
  <div class="tagline">banking and finance lawyers</div>

  <div class="contact">
    <div class="contact__name">Mara Ellison</div>
    <div class="contact__title">Director / CEO</div>
    <ul class="contact__list">
      <li class="contact__item">
        <svg class="contact__icon" viewBox="0 0 20 20" aria-hidden="true"><rect width="20" height="20" rx="3" fill="#0a88cc"/><path d="M5 8c0-2 2-3 5-3s5 1 5 3l-2 1-1-2H8L7 9zM6 10h8l1 5H5z" fill="#fff"/></svg>
        <span>+61-284-3391</span>
      </li>
      <li class="contact__item">
        <svg class="contact__icon" viewBox="0 0 20 20" aria-hidden="true"><rect width="20" height="20" rx="3" fill="#0a88cc"/><path d="M6 4l3 3-1.5 2c1 2 2 3 3.5 3.5L13 11l3 3-2 2C9 16 4 11 4 6z" fill="#fff"/></svg>
        <span>+61-417-2260</span>
      </li>
      <li class="contact__item">
        <svg class="contact__icon" viewBox="0 0 20 20" aria-hidden="true"><rect width="20" height="20" rx="3" fill="#0a88cc"/><rect x="6" y="4" width="8" height="4" fill="#fff"/><rect x="4" y="8" width="12" height="6" rx="1" fill="#fff"/><rect x="6" y="13" width="8" height="3" fill="#fff" stroke="#0a88cc" stroke-width="0.8"/></svg>
        <span>+61-0284-33920</span>
      </li>
      <li class="contact__item">
        <svg class="contact__icon" viewBox="0 0 20 20" aria-hidden="true"><rect width="20" height="20" rx="3" fill="#0a88cc"/><rect x="4" y="6" width="12" height="8" fill="none" stroke="#fff" stroke-width="1.4"/><path d="M4 6l6 5 6-5" fill="none" stroke="#fff" stroke-width="1.4"/></svg>
        <span>info@juriskite.com.au</span>
      </li>
      <li class="contact__item">
        <svg class="contact__icon" viewBox="0 0 20 20" aria-hidden="true"><rect width="20" height="20" rx="3" fill="#0a88cc"/><circle cx="10" cy="10" r="6" fill="none" stroke="#fff" stroke-width="1.3"/><ellipse cx="10" cy="10" rx="2.6" ry="6" fill="none" stroke="#fff" stroke-width="1.1"/><path d="M4 10h12" stroke="#fff" stroke-width="1.1"/></svg>
        <span>www.juriskite.com.au</span>
      </li>
    </ul>
  </div>

  <div class="address-band">Level 14 82 Penhallow Street Sydney NSW 2000</div>
</section>

<section class="card card--back" aria-label="Business card back">
  <div class="brand">
    <span class="brand__square"></span>
    <span class="brand__name">Juriskite</span>
  </div>
  <div class="tagline">banking and finance lawyers</div>
</section>

</body>
</html>
```